Facebook Post for Fence Spring Sale

We have a $12 / FT Fence sale that we have been running for a while now. We need a flyer made up for SPRING.

Our previous flyer can be seen here:
https://media.pixvault-host.example/img/48213907_551903288146720_7391026458813302947_n.jpg?ref=7c21b9e04d8a

We want to use the photos that are shown here https://files.cloudtrove-share.example/view?id=9XkQ7rTmw2LpZdVa4HsE in the flyer. This is to be posted on Facebook so it must be the proper size for Facebook page post.

The wording to be used should be "Spring Fence Sale" and "$12 / FT Wood Fences" Also we should include our business name "Oakridge Fence" and phone number for Free Estimates - 555-314-2076.

Residential Construction

Font styles to use
Serif
Sans Serif

Colors
3176b5
fbee3d
fbed22
fbf289
85cae6
33a6d7

Requirements
Must have
• Phone number, $12 / FT Fence Sale

```html
<!DOCTYPE html>
<html lang="en">
<head>
<meta charset="UTF-8">
<title>Spring Fence Sale – Oakridge Fence</title>
<link rel="stylesheet" href="https://fonts.googleapis.com/css2?family=Montserrat:wght@700;800&family=Raleway:wght@400;500&family=Open+Sans:wght@400;600&display=swap">
<style>
  :root {
    --blue-deep: #3176b5;
    --blue-bright: #33a6d7;
    --sky-light: #85cae6;
    --sky-pale: #d6ecf1;
    --yellow: #fbee22;
    --yellow-soft: #fbf289;
    --white: #ffffff;
    --ink: #1c1c1c;
    --wood: #c9a574;
    --wood-light: #e6d2b0;
    --grass: #5c8a3a;
  }
  * { box-sizing: border-box; margin: 0; padding: 0; }
  html, body {
    width: 1200px;
    height: 1200px;
    overflow: hidden;
    background: var(--white);
  }
  .flyer {
    position: relative;
    width: 1200px;
    height: 1200px;
    overflow: hidden;
    background: var(--white);
  }
  .sky-band {
    position: absolute;
    left: 0; top: 0;
    width: 1200px; height: 625px;
    background: linear-gradient(180deg, var(--sky-pale) 0%, #eaf5f7 55%, var(--white) 100%);
  }
  .price-band {
    position: absolute;
    left: 0; top: 625px;
    width: 1200px; height: 343px;
    background: var(--yellow);
  }
  .contact-band {
    position: absolute;
    left: 0; top: 968px;
    width: 1200px; height: 232px;
    background: var(--blue-deep);
  }
  .headline {
    position: absolute;
    left: 0; top: 50px;
    width: 1200px;
    text-align: center;
  }
  .headline-season {
    display: block;
    font-family: "Raleway", sans-serif;
    font-weight: 400;
    font-size: 128px;
    line-height: 1;
    letter-spacing: 2px;
    color: var(--blue-bright);
  }
  .headline-offer {
    display: block;
    margin-top: 8px;
    font-family: "Montserrat", sans-serif;
    font-weight: 800;
    font-size: 122px;
    line-height: 1;
    letter-spacing: 1px;
    color: var(--blue-deep);
  }
  .gallery {
    position: absolute;
    left: 43px; top: 335px;
    width: 1100px; height: 497px;
    display: flex;
    gap: 25px;
  }
  .gallery-photo {
    flex: 1;
    border: 8px solid var(--white);
    box-shadow: 0 4px 12px rgba(0,0,0,0.35);
  }
  .photo-scalloped {
    background: linear-gradient(180deg, #c8d3cf 0%, var(--wood) 35%, #b89060 65%, var(--grass) 100%);
  }
  .photo-picket-gate {
    background: linear-gradient(180deg, #6b6b5c 0%, var(--wood-light) 25%, #d9c29c 75%, #8f8a7a 100%);
  }
  .photo-split-rail {
    background: linear-gradient(180deg, #2f5a2a 0%, #4d7a3a 35%, var(--wood-light) 55%, var(--grass) 100%);
  }
  .price-line {
    position: absolute;
    left: 0; top: 862px;
    width: 1200px;
    text-align: center;
    font-family: "Open Sans", sans-serif;
    font-weight: 400;
    font-size: 56px;
    line-height: 1;
    color: var(--ink);
  }
  .business-name {
    position: absolute;
    left: 0; top: 1012px;
    width: 1200px;
    text-align: center;
    font-family: "Montserrat", sans-serif;
    font-weight: 700;
    font-size: 62px;
    line-height: 1;
    color: var(--white);
  }
  .estimate-line {
    position: absolute;
    left: 0; top: 1094px;
    width: 1200px;
    text-align: center;
    font-family: "Open Sans", sans-serif;
    font-weight: 400;
    font-size: 44px;
    line-height: 1;
    color: var(--white);
  }
</style>
</head>
<body>
  <main class="flyer">
    <div class="sky-band"></div>
    <div class="price-band"></div>
    <div class="contact-band"></div>

    <h1 class="headline">
      <span class="headline-season">SPRING</span>
      <span class="headline-offer">FENCE SALE</span>
    </h1>

    <section class="gallery">
      <div class="gallery-photo photo-scalloped" role="img" aria-label="Photo of a scalloped wooden privacy fence along a grassy yard"></div>
      <div class="gallery-photo photo-picket-gate" role="img" aria-label="Photo of a wooden picket gate with black hinges"></div>
      <div class="gallery-photo photo-split-rail" role="img" aria-label="Photo of an arched wooden picket gate set in a split-rail fence on a lawn"></div>
    </section>

    <p class="price-line">$12 / FT Wood Fences</p>
    <p class="business-name">OAKRIDGE FENCE</p>
    <p class="estimate-line">FREE ESTIMATES - 555-314-2076</p>
  </main>
</body>
</html>
```